Roofing Company Business Card Design

My husband and I own our own roofing company. We specialise in the supply and installation of metal roofing, fascia, gutter, and downpipes.
I would like our design to somehow incorporate the above things. Having said that the logo also needs to be versatile. I need to be able to use it for uniforms, signage for building sites, and also signage for our cars. So I need it to look good on both a small and large scale.
Looking at logo styles I would like to use either pictorial/combination logo, or emblem logo. With this I would like to try and incorporate the initials "TSC" into this logo somehow.
I would like to use blue, black, and white as my colours.
Industry/Entity Type
Building
Logo Text
Tolvane Steel Cladding Pty Ltd
Logo styles of interest
Emblem Logo
Pictorial/Combination Logo

```html
<!DOCTYPE html>
<html lang="en">
<head>
<meta charset="utf-8">
<title>Tolvane Steel Cladding – Business Card</title>
<link href="https://fonts.googleapis.com/css2?family=Cinzel:wght@500;600&family=Exo+2:wght@600;700&display=swap" rel="stylesheet">
<style>
  :root {
    --page-bg: #e9e4dc;
    --card-white: #ffffff;
    --brand-blue: #0c1599;
    --brand-blue-deep: #07106e;
    --brand-blue-light: #2f3fc2;
    --name-navy: #0d1a8a;
    --steel-grey: #6f7378;
    --steel-light: #c9ccd0;
    --faint-grey: #eceded;
    --text-white: #ffffff;
  }
  * { box-sizing: border-box; margin: 0; padding: 0; }
  html, body { width: 1200px; height: 901px; overflow: hidden; }
  body { background: var(--page-bg); position: relative; font-family: "Cinzel", serif; }

  .card {
    position: absolute;
    width: 518px;
    height: 296px;
    overflow: hidden;
    box-shadow: 3px 4px 6px rgba(0,0,0,0.35);
  }

  /* Front */
  .card-front { left: 149px; top: 139px; background: var(--card-white); }
  .card-front .band { position: absolute; inset: 0; }
  .faint-mark {
    position: absolute; left: 250px; top: 115px;
    font-family: "Exo 2", sans-serif; font-weight: 700;
    font-size: 120px; line-height: 1; color: var(--faint-grey);
    letter-spacing: 2px;
  }
  .brand {
    position: absolute; left: 44px; top: 30px;
    width: 140px; height: 140px;
    display: flex; flex-direction: column; align-items: center; justify-content: center;
  }
  .brand-ring {
    position: absolute; inset: 10px;
    border: 5px solid var(--brand-blue); border-radius: 50%;
  }
  .brand-initials, .brand-name {
    position: relative; font-family: "Exo 2", sans-serif; font-weight: 700;
    color: var(--brand-blue); text-align: center;
  }
  .brand-initials { font-size: 46px; line-height: 1; letter-spacing: 1px; }
  .brand-name { font-size: 10px; line-height: 1.2; width: 96px; }

  .holder { position: absolute; left: 300px; top: 90px; width: 200px; text-align: center; }
  .holder-name { font-size: 22px; font-weight: 500; color: var(--name-navy); letter-spacing: 0.5px; }
  .holder-role {
    margin-top: 6px; font-size: 11px; letter-spacing: 3.5px;
    color: #444; font-weight: 600;
  }
  .contact {
    position: absolute; left: 0; right: 0; top: 240px;
    text-align: center; color: var(--text-white);
    font-size: 12px; line-height: 20px; letter-spacing: 0.4px; font-weight: 500;
  }

  /* Back */
  .card-back { left: 525px; top: 460px; background: var(--brand-blue); }
  .card-back .brand { left: 189px; top: 58px; }
  .card-back .brand-ring { border-color: var(--steel-light); }
  .card-back .brand-initials, .card-back .brand-name { color: var(--text-white); }
  .tagline {
    position: absolute; left: 0; right: 0; top: 233px;
    text-align: center; color: var(--text-white);
    font-family: "Exo 2", sans-serif; font-weight: 600;
    font-size: 13.5px; line-height: 21px; letter-spacing: 0.4px;
  }
</style>
</head>
<body>

<section class="card card-front" aria-label="Business card front">
  <div class="faint-mark" aria-hidden="true">TSC</div>
  <svg class="band" width="518" height="296" viewBox="0 0 518 296" aria-hidden="true">
    <defs>
      <linearGradient id="bandFill" x1="0" y1="0" x2="0" y2="1">
        <stop offset="0" stop-color="var(--brand-blue-light)"/>
        <stop offset="0.45" stop-color="var(--brand-blue)"/>
        <stop offset="1" stop-color="var(--brand-blue-deep)"/>
      </linearGradient>
      <linearGradient id="swooshFill" x1="0" y1="0" x2="1" y2="0">
        <stop offset="0" stop-color="#d8dadd"/>
        <stop offset="0.5" stop-color="var(--steel-grey)"/>
        <stop offset="1" stop-color="#d8dadd"/>
      </linearGradient>
    </defs>
    <path d="M0,226 Q259,158 518,226 Q259,176 0,230 Z" fill="url(#swooshFill)"/>
    <path d="M0,234 Q259,180 518,232 L518,296 L0,296 Z" fill="url(#bandFill)"/>
  </svg>

  <div class="brand">
    <span class="brand-ring"></span>
    <span class="brand-initials">TSC</span>
    <span class="brand-name">Tolvane Steel Cladding</span>
  </div>

  <div class="holder">
    <h1 class="holder-name">Clara Whitmore</h1>
    <p class="holder-role">DIRECTOR</p>
  </div>

  <div class="contact">
    <p>Phone: 0419552076</p>
    <p>Email: clarawhitmore@mailbox.com</p>
  </div>
</section>

<section class="card card-back" aria-label="Business card back">
  <div class="brand">
    <span class="brand-ring"></span>
    <span class="brand-initials">TSC</span>
    <span class="brand-name">Tolvane Steel Cladding</span>
  </div>
  <p class="tagline">Specialising in the Installation of Metal Roofs,<br>Fascia, Gutter, and Downpipes</p>
</section>

</body>
</html>
```